Personal Trainer Business Card

I need a business card using a logo I already have.
The logo is in uploaded files.
Card is to give to prospective clients that interested in health and beauty or already exercise. Would like logo on front or other abstract images and details on back.
Like modern design that also unique and eye catching rather than just generic fitness gym/fitness theme.

Target Market(s)

Main clients are trendy women aged 25-60.

Industry/Entity Type

Fitness

Contact Information for Business Card

Email: tom@tomharvecoaching.com

web: www.tomharvecoaching.com

mobile: 0493 257618

facebook: www.friendlink.net/tomharvecoaching

Location is: Saltwater Bay

Font styles to use
Sans Serif

Colors
000000
1b1b1b
333333

Requirements
Must have
• Logo on front
• black background of sorts on front (fine if mixed with dark grey or abstract)
• White background on back.
Nice to have
• I would like the front side with the logo appearing on it with black background. Fine with alternative ideas and layout.
• Would like the front to be modern, professional and cool/interesting.
• Fine with abstract or modern design.
• Reverse of the card some white background with details on it
• (I like simple fonts).
• CAn use same font colour as in logo in places or what whatever
Should not have
• Avoiding use of cheap pics such as weights

```html
<!DOCTYPE html>
<html lang="en">
<head>
<meta charset="utf-8">
<title>Tom Harve Coaching – Business Card</title>
<link rel="stylesheet" href="https://fonts.googleapis.com/css2?family=Open+Sans:wght@400;700&display=swap">
<style>
  :root {
    --page: #e4e3e0;
    --card-dark: #2d2c2a;
    --card-light: #ffffff;
    --ink: #1b1b1b;
    --gold: #b8955a;
  }
  * { box-sizing: border-box; margin: 0; padding: 0; }
  html, body { width: 1200px; height: 900px; overflow: hidden; }
  body {
    background: var(--page);
    font-family: "Open Sans", sans-serif;
    position: relative;
  }
  .card {
    position: absolute;
    left: 290px;
    width: 620px;
    height: 379px;
    box-shadow: 0 6px 18px rgba(0,0,0,0.18);
  }
  .card-front {
    top: 50px;
    background: var(--card-dark);
    display: flex;
    align-items: center;
    justify-content: center;
  }
  .brand-name {
    color: var(--gold);
    font-weight: 700;
    font-size: 40px;
    letter-spacing: 1px;
    line-height: 1;
    white-space: nowrap;
  }
  .card-back {
    top: 470px;
    background: var(--card-light);
  }
  .contact {
    position: absolute;
    right: 34px;
    bottom: 30px;
    text-align: right;
    color: var(--ink);
  }
  .contact-name {
    font-size: 26px;
    font-weight: 400;
    letter-spacing: 1px;
    line-height: 1.1;
  }
  .contact-role {
    font-size: 18px;
    color: var(--gold);
    margin-bottom: 10px;
  }
  .contact-list { list-style: none; }
  .contact-item {
    display: flex;
    justify-content: flex-end;
    align-items: center;
    gap: 10px;
    font-size: 16px;
    line-height: 26px;
    white-space: nowrap;
  }
  .contact-icon {
    width: 16px;
    height: 16px;
    fill: var(--gold);
    flex: none;
  }
</style>
</head>
<body>
  <section class="card card-front">
    <div class="brand-name">Tom Harve Coaching</div>
  </section>

  <section class="card card-back">
    <div class="contact">
      <div class="contact-name">TOM HARVE</div>
      <div class="contact-role">Personal Trainer</div>
      <ul class="contact-list">
        <li class="contact-item">Saltwater Bay
          <svg class="contact-icon" viewBox="0 0 16 16" aria-hidden="true"><path d="M8 0a5.5 5.5 0 0 0-5.5 5.5C2.5 10 8 16 8 16s5.5-6 5.5-10.5A5.5 5.5 0 0 0 8 0zm0 8a2.5 2.5 0 1 1 0-5 2.5 2.5 0 0 1 0 5z"/></svg>
        </li>
        <li class="contact-item">0493 257618
          <svg class="contact-icon" viewBox="0 0 16 16" aria-hidden="true"><path d="M4 0h8a1 1 0 0 1 1 1v14a1 1 0 0 1-1 1H4a1 1 0 0 1-1-1V1a1 1 0 0 1 1-1zm1 2v9h6V2H5zm3 10.5a1 1 0 1 0 0 2 1 1 0 0 0 0-2z"/></svg>
        </li>
        <li class="contact-item">tom@tomharvecoaching.com
          <svg class="contact-icon" viewBox="0 0 16 16" aria-hidden="true"><path d="M0 3h16v10H0V3zm1.5 1.2L8 9l6.5-4.8V4h-13v.2z"/></svg>
        </li>
        <li class="contact-item">www.tomharvecoaching.com
          <svg class="contact-icon" viewBox="0 0 16 16" aria-hidden="true"><path d="M8 0a8 8 0 1 0 0 16A8 8 0 0 0 8 0zm5.9 7.3h-2.6a12 12 0 0 0-.9-4.8 6.5 6.5 0 0 1 3.5 4.8zM8 1.5c.8 1 1.6 3 1.8 5.8H6.2C6.4 4.5 7.2 2.5 8 1.5zM5.6 2.5a12 12 0 0 0-.9 4.8H2.1a6.5 6.5 0 0 1 3.5-4.8zM2.1 8.7h2.6a12 12 0 0 0 .9 4.8 6.5 6.5 0 0 1-3.5-4.8zM8 14.5c-.8-1-1.6-3-1.8-5.8h3.6c-.2 2.8-1 4.8-1.8 5.8zm2.4-1a12 12 0 0 0 .9-4.8h2.6a6.5 6.5 0 0 1-3.5 4.8z"/></svg>
        </li>
        <li class="contact-item">www.friendlink.net/tomharvecoaching
          <svg class="contact-icon" viewBox="0 0 16 16" aria-hidden="true"><rect x="1" y="1" width="14" height="14" rx="1"/></svg>
        </li>
      </ul>
    </div>
  </section>
</body>
</html>
```